Create New Bussiness Card For New Shoes Store

Vandrel is a store that sells a variety of skateboard shoes such as Kolvo, Frisk etc. we also sell some skateboard and all skateboard accessories.
we like black and white style logo, but also like blue as well.
We are fully assembled with a deck, truck, wheels, and bearings. Add some personality to your board with a fun, graphic skateboard deck. Constructed of thick 7 ply maple,
Target Market(s)
Target audience: 12-40 year old
especially for young man
Industry/Entity Type
Industrial
Contact Information for Business Card
Name: Vandrel
Address1: 2493 Marlow Pike Rd
City: Halbrook
State: Delmont
Zip: 48217
Country: US
Phone: 614583062
email: danbrellick@quortmail.example

```html
<!DOCTYPE html>
<html lang="en">
<head>
<meta charset="utf-8">
<title>Vandrel Business Card</title>
<link href="https://fonts.googleapis.com/css2?family=Montserrat:wght@400&display=swap" rel="stylesheet">
<style>
  :root {
    --backdrop: #c8914f;
    --card-dark: #1b1b1c;
    --card-light: #ffffff;
    --accent: #b565b0;
  }
  html, body {
    margin: 0;
    width: 1200px;
    height: 1200px;
    overflow: hidden;
    background: var(--backdrop);
    font-family: "Montserrat", sans-serif;
  }
  .card {
    position: absolute;
    top: 448px;
    width: 480px;
    height: 274px;
    box-shadow: 0 10px 22px rgba(0,0,0,0.35);
    overflow: hidden;
  }
  .card-front {
    left: 78px;
    background: var(--card-dark);
    display: flex;
    align-items: center;
    justify-content: center;
  }
  .card-back {
    left: 642px;
    background: var(--card-light);
  }
  .wordmark {
    display: flex;
    align-items: center;
    gap: 12px;
    color: var(--accent);
    font-weight: 400;
    letter-spacing: 1px;
    white-space: nowrap;
  }
  .wordmark-dot {
    display: block;
    border: 2px solid var(--accent);
    border-radius: 50%;
    box-sizing: border-box;
  }
  .card-front .wordmark { font-size: 44px; }
  .card-front .wordmark-dot { width: 28px; height: 28px; }
  .back-top {
    height: 166px;
    display: flex;
    align-items: center;
    justify-content: center;
  }
  .card-back .wordmark { font-size: 28px; gap: 8px; }
  .card-back .wordmark-dot { width: 18px; height: 18px; }
  .back-bottom {
    position: relative;
    height: 108px;
    background: var(--card-dark);
    color: var(--accent);
  }
  .back-name {
    position: absolute;
    left: 49px;
    top: 36px;
    font-size: 22px;
    margin: 0;
    font-weight: 400;
  }
  .contact-list {
    position: absolute;
    left: 259px;
    top: 16px;
    margin: 0;
    padding: 0;
    list-style: none;
    font-size: 11px;
    line-height: 12px;
    white-space: nowrap;
  }
</style>
</head>
<body>
  <section class="card card-front">
    <div class="wordmark"><span class="wordmark-dot"></span>Vandrel</div>
  </section>

  <section class="card card-back">
    <div class="back-top">
      <div class="wordmark"><span class="wordmark-dot"></span>Vandrel</div>
    </div>
    <div class="back-bottom">
      <h2 class="back-name">Vandrel</h2>
      <ul class="contact-list">
        <li>Address: 2493 Marlow Pike Rd</li>
        <li>City: Halbrook</li>
        <li>State: Delmont</li>
        <li>Zip: 48217</li>
        <li>Country: US</li>
        <li>Phone: 614583062</li>
      </ul>
    </div>
  </section>
</body>
</html>
```